Brightbuns Business Card Design

Our company is called Brightbuns. We manufacture confectionary snacks & frozen novelties. Our initial product portfolio includes frozen ice lollies/popsicles & stick ice cream bars.

We require a business card design.

Please use the attached Logo.

Please use an orange, brown, yellow colour code. You may choose any combination of the 3 or include all three. The logo however must remain orange.

Target Market(s)

Business card will be targeted at distributors of our products such as supermarket procurement managers, convenience store owners, wholesale distributors and merchandising agents.

Industry/Entity Type

Business

Requirements
Must have
• Kelvin Marsh_Director/ P.O.Box Westhollow 5172, Accra, Ghana / m: 00233(0)507318264/ e: kelvin.marsh@fernpost.co.uk

```html
<!DOCTYPE html>
<html lang="en">
<head>
<meta charset="utf-8">
<title>Brightbuns Business Card</title>
<link rel="stylesheet" href="https://fonts.googleapis.com/css2?family=Comfortaa:wght@700&family=Montserrat:wght@400&display=swap">
<style>
  :root {
    --page-bg: #d9d6d2;
    --card-brown: #672c16;
    --card-brown-deep: #5a2612;
    --brand-orange: #ea7128;
    --soft-orange: #e0803f;
    --card-radius: 26px;
  }
  * { box-sizing: border-box; margin: 0; padding: 0; }
  html, body {
    width: 1200px;
    height: 900px;
    overflow: hidden;
    background: var(--page-bg);
  }
  .stage {
    position: relative;
    width: 1200px;
    height: 900px;
    display: flex;
    flex-direction: column;
    align-items: center;
    justify-content: center;
    gap: 56px;
  }
  .card {
    position: relative;
    width: 640px;
    height: 366px;
    border-radius: var(--card-radius);
    background: linear-gradient(160deg, var(--card-brown) 0%, var(--card-brown-deep) 100%);
    box-shadow: 0 10px 24px rgba(0, 0, 0, 0.25);
    overflow: hidden;
  }
  .card-front {
    display: flex;
    align-items: center;
    justify-content: center;
  }
  .brand-name {
    font-family: "Comfortaa", sans-serif;
    font-weight: 700;
    font-size: 64px;
    color: var(--brand-orange);
    letter-spacing: 0.5px;
  }
  .card-back .person {
    position: absolute;
    left: 58px;
    top: 58px;
  }
  .person-name {
    font-family: "Comfortaa", sans-serif;
    font-weight: 700;
    font-size: 27px;
    color: var(--brand-orange);
  }
  .person-role {
    font-family: "Montserrat", sans-serif;
    font-weight: 400;
    font-size: 17px;
    color: var(--soft-orange);
    margin-top: 4px;
    letter-spacing: 0.6px;
  }
  .contact-list {
    position: absolute;
    left: 58px;
    top: 190px;
    display: grid;
    grid-template-columns: 108px auto;
    row-gap: 14px;
  }
  .contact-label {
    font-family: "Comfortaa", sans-serif;
    font-weight: 700;
    font-size: 15px;
    color: var(--brand-orange);
    text-align: right;
    padding-right: 22px;
  }
  .contact-value {
    font-family: "Montserrat", sans-serif;
    font-weight: 400;
    font-size: 17px;
    line-height: 1.15;
    color: var(--soft-orange);
    letter-spacing: 0.6px;
  }
</style>
</head>
<body>
  <main class="stage">
    <section class="card card-front" aria-label="Business card front">
      <span class="brand-name">Brightbuns</span>
    </section>

    <section class="card card-back" aria-label="Business card back">
      <div class="person">
        <h1 class="person-name">Kelvin Marsh</h1>
        <p class="person-role">Director</p>
      </div>
      <dl class="contact-list">
        <dt class="contact-label">mobile</dt>
        <dd class="contact-value">00233(0)507318264</dd>
        <dt class="contact-label">email</dt>
        <dd class="contact-value">kelvin.marsh@fernpost.co.uk</dd>
        <dt class="contact-label">address</dt>
        <dd class="contact-value">P.O.Box Westhollow 5172,<br>Accra, Ghana</dd>
      </dl>
    </section>
  </main>
</body>
</html>
```